Attention grabbing 6x9 postcard

We are looking to have an attention grabbing post card that be sent out to homeowners from our roofing company Olum Roofing. the concept is that on the front it will say something like (STOP THE KNOCKING!
Tired of roofers knocking on your door? Contact us because we value your time as much as you value the roof over your head."
Olum Roofing
OlumRoofing.com
877.612.OLUM
info@olumroofing.com

Please feel free to come up with something very creative. Once we pick the final design we will provide the copy.

```html
<!DOCTYPE html>
<html lang="en">
<head>
<meta charset="utf-8">
<title>Olum Roofing Postcard</title>
<link rel="stylesheet" href="https://fonts.googleapis.com/css2?family=Poppins:wght@400;600;700;800&display=swap">
<style>
  :root {
    --stage: #71767a;
    --gold: #e9b338;
    --ink: #0c0c0c;
    --paper: #ffffff;
    --stamp: #e2e3e5;
    --rule: #6a6a6a;
  }
  html, body {
    margin: 0;
    width: 1200px;
    height: 1200px;
    overflow: hidden;
    background: var(--stage);
  }
  .postcard {
    position: absolute;
    left: 238px;
    width: 723px;
    height: 488px;
    display: block;
    font-family: 'Poppins', sans-serif;
  }
  .postcard--front { top: 91px; }
  .postcard--back { top: 617px; }
  .gold { fill: var(--gold); }
  .ink { fill: var(--ink); }
  .paper { fill: var(--paper); }
  .brand-name { fill: var(--ink); font-weight: 700; letter-spacing: 0; }
  .headline { font-weight: 800; letter-spacing: -1px; }
  .subhead { font-weight: 700; fill: var(--ink); }
  .body-copy { font-weight: 400; fill: var(--ink); }
  .phone-number { font-weight: 700; }
  .contact { font-weight: 400; }
  .service-label { font-weight: 700; fill: var(--paper); }
  .section-title { font-weight: 800; fill: var(--ink); }
</style>
</head>
<body>

<svg class="postcard postcard--front" viewBox="0 0 1163 786" xmlns="http://www.w3.org/2000/svg">
  <defs>
    <linearGradient id="roofTone" x1="0" y1="0" x2="1" y2="1">
      <stop offset="0" stop-color="#b9bcc4"/>
      <stop offset="0.5" stop-color="#6c7079"/>
      <stop offset="1" stop-color="#3e424a"/>
    </linearGradient>
    <linearGradient id="shingleTone" x1="0" y1="0" x2="0" y2="1">
      <stop offset="0" stop-color="#7d8796"/>
      <stop offset="1" stop-color="#4d5663"/>
    </linearGradient>
  </defs>

  <rect class="ink" width="1163" height="786"/>

  <polygon class="paper" points="0,0 487,0 487,300 110,300 0,245"/>
  <polygon class="gold" points="0,230 110,292 95,294 0,242"/>
  <text class="brand-name" x="262" y="170" font-size="46" text-anchor="middle">Olum Roofing</text>

  <polyline points="497,0 497,385 850,575" fill="none" stroke="#fff" stroke-width="5"/>
  <polygon points="520,0 1163,0 1163,400 975,560 840,560 520,378" fill="url(#roofTone)" role="img" aria-label="Photo of a roofer in a safety harness laying asphalt shingles"/>
  <polygon class="paper" points="1163,415 1163,620 1045,682 1000,682 1100,590"/>
  <polygon class="ink" points="1163,430 1163,610 1045,672 1010,672 1110,585"/>

  <text class="headline gold" x="58" y="405" font-size="82">STOP THE</text>
  <text class="headline paper" x="58" y="478" font-size="78">KNOCKING!</text>

  <polygon class="gold" points="0,513 742,513 835,572 0,572"/>
  <text class="subhead" x="63" y="552" font-size="28">Tired of roofers knocking on your door?</text>

  <polygon class="paper" points="0,572 835,572 1005,672 0,672"/>
  <polygon class="gold" points="800,572 814,572 930,640 918,640"/>
  <text class="body-copy" x="63" y="613" font-size="24">Contact us because we value your time as much as you value</text>
  <text class="body-copy" x="63" y="642" font-size="24">the roof over your head.</text>

  <polygon class="paper" points="975,337 1113.6,417 1113.6,577 975,657 836.4,577 836.4,417"/>
  <polygon class="ink" points="975,351 1101.4,424 1101.4,570 975,643 848.6,570 848.6,424"/>
  <polygon points="975,370 1085,433.5 1085,560.5 975,624 865,560.5 865,433.5" fill="url(#shingleTone)" role="img" aria-label="Close-up of grey asphalt roof shingles"/>

  <polygon class="gold" points="520,690 1045,690 1163,628 1163,786 500,786 600,738"/>
  <polygon class="paper" points="470,672 505,672 600,738 500,786 470,786 565,738"/>
  <rect class="ink" x="0" y="672" width="470" height="114"/>
  <polygon class="ink" points="470,672 565,738 470,786"/>

  <g transform="translate(87,727)">
    <polygon class="paper" points="0,-30 26,-15 26,15 0,30 -26,15 -26,-15"/>
    <polygon class="gold" points="0,-25 21.6,-12.5 21.6,12.5 0,25 -21.6,12.5 -21.6,-12.5"/>
    <path class="ink" transform="translate(-14,-14) scale(1.15)" d="M6.6 10.8c1.4 2.8 3.8 5.1 6.6 6.6l2.2-2.2c.3-.3.7-.4 1-.2 1.1.4 2.3.6 3.6.6.6 0 1 .4 1 1V20c0 .6-.4 1-1 1C10.6 21 3 13.4 3 4c0-.6.4-1 1-1h3.5c.6 0 1 .4 1 1 0 1.3.2 2.5.6 3.6.1.3 0 .7-.2 1z"/>
  </g>
  <text class="phone-number paper" x="130" y="746" font-size="56">877.612.OLUM</text>

  <g transform="translate(643,725)" fill="none" stroke="#0c0c0c" stroke-width="1.8">
    <circle r="10"/><ellipse rx="4.5" ry="10"/><line x1="-10" y1="0" x2="10" y2="0"/>
  </g>
  <text class="contact ink" x="663" y="732" font-size="20">OlumRoofing.com</text>
  <g transform="translate(868,725)">
    <circle class="ink" r="11"/>
    <rect x="-6.5" y="-4.5" width="13" height="9" fill="none" stroke="#fff" stroke-width="1.6"/>
    <polyline points="-6.5,-4.5 0,1 6.5,-4.5" fill="none" stroke="#fff" stroke-width="1.6"/>
  </g>
  <text class="contact ink" x="886" y="732" font-size="20">info@olumroofing.com</text>
</svg>

<svg class="postcard postcard--back" viewBox="0 0 1163 786" xmlns="http://www.w3.org/2000/svg">
  <defs>
    <linearGradient id="panelTone" x1="0" y1="0" x2="1" y2="0">
      <stop offset="0" stop-color="#111"/>
      <stop offset="0.5" stop-color="#2a2a2a"/>
      <stop offset="1" stop-color="#0d0d0d"/>
    </linearGradient>
    <linearGradient id="houseTone" x1="0" y1="0" x2="0" y2="1">
      <stop offset="0" stop-color="#8fa4bd"/><stop offset="1" stop-color="#8a7d6a"/>
    </linearGradient>
    <linearGradient id="stormTone" x1="0" y1="0" x2="0" y2="1">
      <stop offset="0" stop-color="#b6bcc6"/><stop offset="1" stop-color="#4f5661"/>
    </linearGradient>
    <linearGradient id="buildTone" x1="0" y1="0" x2="0" y2="1">
      <stop offset="0" stop-color="#7aa0cf"/><stop offset="1" stop-color="#7a5d42"/>
    </linearGradient>
    <linearGradient id="tarpTone" x1="0" y1="0" x2="0" y2="1">
      <stop offset="0" stop-color="#3f6a3a"/><stop offset="0.5" stop-color="#4d8fd6"/><stop offset="1" stop-color="#6e6e6e"/>
    </linearGradient>
  </defs>

  <rect class="paper" width="1163" height="786"/>

  <polygon fill="url(#panelTone)" points="0,85 500,85 645,170 645,330 610,352 610,618 645,640 645,786 0,786"/>
  <polygon class="gold" points="0,0 395,0 645,145 645,168 500,85 0,85"/>
  <rect class="gold" x="621" y="352" width="13" height="266"/>
  <text class="section-title" x="42" y="68" font-size="42">OUR SERVICES</text>

  <line x1="310" y1="120" x2="310" y2="600" stroke="var(--rule)" stroke-width="1.5"/>
  <line x1="57" y1="350" x2="537" y2="350" stroke="var(--rule)" stroke-width="1.5"/>

  <g stroke="var(--gold)" stroke-width="2.5">
    <polygon fill="url(#houseTone)" points="162,104 234.7,146 234.7,230 162,272 89.3,230 89.3,146" role="img" aria-label="Photo of a house roof gable"/>
    <polygon fill="url(#stormTone)" points="460,104 532.7,146 532.7,230 460,272 387.3,230 387.3,146" role="img" aria-label="Photo of storm damaged shingles"/>
    <polygon fill="url(#buildTone)" points="162,368 234.7,410 234.7,494 162,536 89.3,494 89.3,410" role="img" aria-label="Photo of a house under construction"/>
    <polygon fill="url(#tarpTone)" points="460,368 532.7,410 532.7,494 460,536 387.3,494 387.3,410" role="img" aria-label="Photo of a roof covered with a blue repair tarp"/>
  </g>

  <g font-size="21" text-anchor="middle">
    <text class="service-label" x="162" y="299">Retail/commercial</text>
    <text class="service-label" x="162" y="327">Roof replacement</text>
    <text class="service-label" x="460" y="299">Storm Damage</text>
    <text class="service-label" x="460" y="324">Roof Replacement</text>
    <text class="service-label" x="162" y="568">New</text>
    <text class="service-label" x="162" y="593">Construction</text>
    <text class="service-label" x="460" y="562">Repairs &amp;</text>
    <text class="service-label" x="460" y="587">Restoration</text>
  </g>

  <polygon class="gold" points="0,628 610,628 645,650 645,700 0,700"/>
  <g transform="translate(92,664)">
    <polygon class="ink" points="0,-28 24.2,-14 24.2,14 0,28 -24.2,14 -24.2,-14"/>
    <path fill="var(--gold)" transform="translate(-13,-13) scale(1.1)" d="M6.6 10.8c1.4 2.8 3.8 5.1 6.6 6.6l2.2-2.2c.3-.3.7-.4 1-.2 1.1.4 2.3.6 3.6.6.6 0 1 .4 1 1V20c0 .6-.4 1-1 1C10.6 21 3 13.4 3 4c0-.6.4-1 1-1h3.5c.6 0 1 .4 1 1 0 1.3.2 2.5.6 3.6.1.3 0 .7-.2 1z"/>
  </g>
  <text class="phone-number ink" x="136" y="689" font-size="62">877.612.OLUM</text>

  <g transform="translate(87,731)" fill="none" stroke="var(--gold)" stroke-width="1.8">
    <circle r="10"/><ellipse rx="4.5" ry="10"/><line x1="-10" y1="0" x2="10" y2="0"/>
  </g>
  <text class="contact paper" x="107" y="738" font-size="21">OlumRoofing.com</text>
  <g transform="translate(323,731)" fill="none" stroke="var(--gold)" stroke-width="1.8">
    <rect x="-9" y="-7" width="18" height="14"/>
    <polyline points="-9,-7 0,1 9,-7"/>
  </g>
  <text class="contact paper" x="343" y="738" font-size="21">info@olumroofing.com</text>

  <text class="brand-name" x="810" y="150" font-size="28" text-anchor="middle">Olum Roofing</text>
  <rect x="977" y="79" width="121" height="121" fill="var(--stamp)"/>
</svg>

</body>
</html>
```